New Packaging Design Project

Wine packaging redesign. Retail partner requested a redesign of a private label wine. The old label is attached. Our partner liked the Lantern and Briar label and wanted something similar. There will be a logo added to the top of the label

Went on vacation/holiday

```html
<!DOCTYPE html>
<html lang="en">
<head>
<meta charset="utf-8">
<title>Red Blend Wine Label</title>
<link rel="stylesheet" href="https://fonts.googleapis.com/css2?family=Montserrat:wght@500&family=Oswald:wght@400&family=Roboto+Condensed:wght@300&family=Tinos&display=swap">
<style>
  :root {
    --page: #ffffff;
    --label-light: #606063;
    --label-mid: #535356;
    --label-dark: #3c3c3f;
    --band-dark: #2f2f32;
    --gold: #e9c86a;
    --gold-deep: #c9892e;
    --frame: #d08a3a;
    --red: #d42a22;
    --white: #f4f4f4;
    --photo-light: #b9b9b9;
    --photo-mid: #8c8c8c;
    --photo-dark: #5e5e5e;
  }
  * { margin: 0; padding: 0; box-sizing: border-box; }
  html, body {
    width: 1200px;
    height: 1172px;
    overflow: hidden;
    background: var(--page);
  }
  .canvas {
    position: relative;
    width: 1200px;
    height: 1172px;
  }
  .wine-label {
    position: absolute;
    left: 279px;
    top: 35px;
    width: 642px;
    height: 1102px;
    overflow: hidden;
    background: linear-gradient(180deg, var(--label-dark) 0%, var(--label-mid) 18%, var(--label-light) 55%, var(--label-mid) 100%);
  }
  .label-shading {
    position: absolute;
    inset: 0;
    background: linear-gradient(90deg, rgba(0,0,0,0.12) 0%, rgba(0,0,0,0) 30%, rgba(0,0,0,0) 70%, rgba(0,0,0,0.25) 100%);
  }
  .lower-band {
    position: absolute;
    left: 0;
    top: 812px;
    width: 100%;
    height: 62px;
    background: linear-gradient(180deg, var(--band-dark) 0%, rgba(60,60,63,0.4) 60%, rgba(90,90,93,0) 100%);
  }
  .accent-lines {
    position: absolute;
    inset: 0;
    width: 642px;
    height: 1102px;
  }
  .region-title {
    position: absolute;
    top: 178px;
    left: 0;
    width: 100%;
    padding-left: 12px;
    text-align: center;
    font-family: "Montserrat", sans-serif;
    font-weight: 500;
    font-size: 52px;
    letter-spacing: 3px;
    color: var(--gold);
  }
  .scene-frame {
    position: absolute;
    left: 49px;
    top: 249px;
    width: 540px;
    height: 355px;
    border: 3px solid var(--frame);
    padding: 3px;
  }
  .scene-photo {
    width: 100%;
    height: 100%;
    background: linear-gradient(180deg, var(--photo-dark) 0%, var(--photo-mid) 38%, var(--photo-light) 60%, var(--photo-mid) 100%);
  }
  .blend-name {
    position: absolute;
    top: 614px;
    left: 0;
    width: 100%;
    text-align: center;
    font-family: "Oswald", sans-serif;
    font-weight: 400;
    font-size: 56px;
    letter-spacing: -1px;
    color: var(--red);
  }
  .varietals {
    position: absolute;
    left: 0;
    width: 100%;
    text-align: center;
    font-family: "Roboto Condensed", sans-serif;
    font-weight: 300;
    font-size: 33px;
    color: var(--gold);
    white-space: nowrap;
  }
  .varietals-first { top: 722px; padding-left: 10px; word-spacing: 2px; }
  .varietals-second { top: 766px; left: -14px; width: 670px; }
  .varietals .divider { color: rgba(233,200,106,0.5); margin: 0 10px; }
  .vintage {
    position: absolute;
    top: 926px;
    left: 0;
    width: 100%;
    text-align: center;
    font-family: "Tinos", serif;
    font-size: 31px;
    color: var(--white);
  }
</style>
</head>
<body>
<main class="canvas">
  <section class="wine-label">
    <div class="label-shading"></div>
    <div class="lower-band"></div>

    <svg class="accent-lines" viewBox="0 0 642 1102" aria-hidden="true">
      <!-- top left sweep -->
      <polygon points="0,150 140,0 250,0 0,250" fill="#333336" opacity="0.55"/>
      <line x1="0" y1="212" x2="250" y2="12" stroke="var(--gold-deep)" stroke-width="3"/>
      <line x1="0" y1="232" x2="230" y2="40" stroke="var(--gold)" stroke-width="1.5"/>
      <line x1="0" y1="300" x2="120" y2="200" stroke="var(--gold-deep)" stroke-width="1.2" opacity="0.7"/>
      <rect x="0" y="0" width="44" height="40" fill="#7a6a3c" opacity="0.45"/>
      <!-- bottom right sweep -->
      <polygon points="642,870 642,980 460,1102 330,1102" fill="#333336" opacity="0.5"/>
      <line x1="360" y1="1102" x2="642" y2="856" stroke="var(--gold-deep)" stroke-width="3"/>
      <line x1="392" y1="1102" x2="642" y2="884" stroke="var(--gold)" stroke-width="1.5"/>
      <line x1="420" y1="1102" x2="642" y2="910" stroke="var(--gold-deep)" stroke-width="1.2" opacity="0.7"/>
      <rect x="598" y="1040" width="44" height="62" fill="#7a6a3c" opacity="0.45"/>
    </svg>

    <h1 class="region-title">NAPA VALLEY</h1>

    <figure class="scene-frame">
      <div class="scene-photo" role="img" aria-label="Black-and-white beach scene with palm trees, a thatched hut and a lounge chair on the sand"></div>
    </figure>

    <h2 class="blend-name">RED BLED</h2>

    <p class="varietals varietals-first">MERLOT&nbsp;&nbsp; CABERENT SAUVIGNON</p>
    <p class="varietals varietals-second">CABERNET FRAN<span class="divider">|</span>PETIT VERDOT<span class="divider">|</span>MALBEC</p>

    <p class="vintage">2018</p>
  </section>
</main>
</body>
</html>
```